Business Card Design For Marketing Agnecy LWP

Need business card design for marketing agency.

Dorian Pellow
President, CEO
1-555-302-4196
dorian@brightlanepromotions.example
www.BrightlanePromotions.example

Back Side:
Boost Sales Using Rewards, Incentives & Giveaways
Get A Free Sample Package

Target Market(s)

B2B

Industry/Entity Type

Marketing

Contact Information for Business Card

Dorian Pellow
President, CEO
1-555-302-4196

Back Side:
Get A Free Sample Package

Please note that my current url is OLD DESIGN. I am working on new design and want the business card to match color themes at least on new site. Here is the demo link for new site so you can see the colors I use, etc.

http://pixelquarrydemo.example/dh/dorian/lwp_final/index.html

Requirements
Must have
• Please note that my current url is OLD DESIGN. I am working on new design and want the business card to match color themes at least on new site. Here is the demo link for new site so you can see the colors I use, etc.

Nice to have

Should not have

```html
<!DOCTYPE html>
<html lang="en">
<head>
<meta charset="utf-8">
<title>Brightlane Promotions — Business Card</title>
<link rel="stylesheet" href="https://fonts.googleapis.com/css2?family=Montserrat:wght@400;500;600;700&display=swap">
<style>
  :root {
    --brand-blue: #2a7bc0;
    --ink: #333333;
    --card-white: #ffffff;
    --card-dark-top: #4a4a4a;
    --card-dark-bottom: #2c2c2c;
    --page: #ffffff;
  }
  * { margin: 0; padding: 0; box-sizing: border-box; }
  html, body {
    width: 1200px;
    height: 840px;
    overflow: hidden;
    background: var(--page);
    font-family: "Montserrat", sans-serif;
  }
  .canvas {
    position: relative;
    width: 1200px;
    height: 840px;
  }
  .card {
    position: absolute;
    top: 232px;
    width: 364px;
    height: 364px;
    border-radius: 10px;
  }
  .card--front {
    left: 204px;
    background: var(--card-white);
    border: 1px solid #e6e6e6;
    color: var(--ink);
    text-align: center;
  }
  .card--back {
    left: 632px;
    background: linear-gradient(160deg, var(--card-dark-top), var(--card-dark-bottom));
  }
  .front-wordmark {
    position: absolute;
    top: 62px;
    left: 0;
    width: 100%;
    font-weight: 600;
    font-size: 21px;
    letter-spacing: 0.5px;
    color: var(--brand-blue);
  }
  .contact-name {
    position: absolute;
    top: 186px;
    left: 0;
    width: 100%;
    font-weight: 600;
    font-size: 18px;
    letter-spacing: 0.4px;
    color: var(--brand-blue);
  }
  .contact-title {
    position: absolute;
    top: 210px;
    left: 0;
    width: 100%;
    font-size: 13px;
  }
  .contact-icons {
    position: absolute;
    top: 244px;
    left: 0;
    width: 100%;
    display: flex;
    justify-content: center;
    gap: 7px;
  }
  .contact-lines {
    position: absolute;
    top: 270px;
    left: 0;
    width: 100%;
    font-size: 13px;
    line-height: 18.5px;
  }
  .back-monogram {
    position: absolute;
    top: 80px;
    left: 0;
    width: 100%;
    text-align: center;
    font-weight: 600;
    font-size: 104px;
    line-height: 1;
    letter-spacing: 2px;
    color: var(--brand-blue);
  }
  .back-wordmark {
    position: absolute;
    top: 248px;
    left: 0;
    width: 100%;
    text-align: center;
    font-weight: 600;
    font-size: 20px;
    letter-spacing: 0.5px;
    color: var(--brand-blue);
  }
</style>
</head>
<body>
<main class="canvas">
  <section class="card card--front">
    <div class="front-wordmark">BRIGHTLANE PROMOTIONS</div>
    <div class="contact-name">DORIAN PELLOW</div>
    <div class="contact-title">President, CEO</div>
    <div class="contact-icons">
      <svg width="15" height="15" viewBox="0 0 15 15" aria-label="Phone">
        <rect width="15" height="15" rx="2.5" fill="var(--brand-blue)"/>
        <path d="M4.5 3.2c.5-.3 1 .1 1.2.6l.5 1.3c.1.4-.1.7-.4.9l-.4.3c.4 1.2 1.3 2.2 2.5 2.7l.3-.4c.3-.3.6-.4 1-.3l1.2.6c.5.2.8.7.5 1.2-.5.9-1.4 1.2-2.3.9C6.4 10.2 4.6 8.4 3.9 6.1c-.3-1 .1-2.3.6-2.9z" fill="#fff"/>
      </svg>
      <svg width="15" height="15" viewBox="0 0 15 15" aria-label="Email">
        <rect width="15" height="15" rx="2.5" fill="var(--brand-blue)"/>
        <rect x="3.2" y="4.5" width="8.6" height="6" rx="0.8" fill="none" stroke="#fff" stroke-width="1.1"/>
        <path d="M3.6 5l3.9 3 3.9-3" fill="none" stroke="#fff" stroke-width="1.1"/>
      </svg>
      <svg width="15" height="15" viewBox="0 0 15 15" aria-label="Website">
        <rect width="15" height="15" rx="2.5" fill="var(--brand-blue)"/>
        <g fill="none" stroke="#fff" stroke-width="0.9">
          <circle cx="7.5" cy="7.5" r="4.2"/>
          <ellipse cx="7.5" cy="7.5" rx="1.8" ry="4.2"/>
          <path d="M3.3 7.5h8.4M4 5.4h7M4 9.6h7"/>
        </g>
      </svg>
    </div>
    <div class="contact-lines">
      <div>1-555-302-4196</div>
      <div>www.BrightlanePromotions.example</div>
      <div>dorian@brightlanepromotions.example</div>
    </div>
  </section>

  <section class="card card--back">
    <div class="back-monogram">LWP</div>
    <div class="back-wordmark">BRIGHTLANE PROMOTIONS</div>
  </section>
</main>
</body>
</html>
```